UNIQUE, Elegant business card for transport company.

MUST BE AN ACTUAL GRAPHIC DESIGNER.
NO TEMPLATES, NO MOCKUP GENERATORS.
Looking for a top notch, head turning, business card.
Will be printed on premium luxury paper with spot glossing and debossing.
Must know how to set up for spot glossing. Must be willing to work on the file to meet printers spec after final design.

Target Market(s)

All info on .psd file

Contact Information for Business Card

All info on .psd file

Requirements
Must have
• All info on .psd file
Nice to have
• All info on .psd file
Should not have
• Nothing red

```html
<!DOCTYPE html>
<html lang="en">
<head>
<meta charset="UTF-8">
<title>Norvane Transport – Business Card</title>
<link href="https://fonts.googleapis.com/css2?family=Montserrat:wght@300;400;600;700&family=Oswald:wght@600&display=swap" rel="stylesheet">
<style>
  :root {
    --bg: #141414;
    --card: #1c1c1c;
    --card-edge: #262626;
    --silver: #c9c9c9;
    --silver-dim: #9a9a9a;
    --silver-bright: #e6e6e6;
    --accent: #3a9ee0;
    --rule: #7a7a7a;
  }
  * { margin: 0; padding: 0; box-sizing: border-box; }
  html, body {
    width: 1200px; height: 900px; overflow: hidden;
    background: radial-gradient(ellipse at 60% 40%, #1e1e1e 0%, var(--bg) 70%);
    font-family: "Montserrat", sans-serif;
    color: var(--silver);
  }
  .card {
    position: absolute; left: 250px; width: 700px; height: 400px;
    background: linear-gradient(135deg, var(--card) 0%, #222 60%, var(--card) 100%);
    border: 1px solid var(--card-edge);
    box-shadow: 0 18px 40px rgba(0,0,0,.6);
  }
  .card--front { top: 30px; }
  .card--back { top: 470px; }

  /* front */
  .tagline {
    position: absolute; top: 40px; left: 60px; right: 60px; text-align: center;
    font-weight: 700; font-size: 25px; letter-spacing: 1.5px; color: var(--silver);
  }
  .tagline__sub {
    display: flex; align-items: center; gap: 10px; margin-top: 6px;
    font-weight: 400; font-size: 15px; letter-spacing: 1px; color: var(--silver-dim);
  }
  .tagline__sub::before, .tagline__sub::after {
    content: ""; flex: 1; height: 1px; background: var(--rule);
  }
  .brand-mark {
    position: absolute; top: 165px; left: 0; right: 0;
    display: flex; justify-content: center; align-items: center; gap: 14px;
  }
  .brand-mark__dot { width: 22px; height: 22px; border-radius: 50%; background: var(--accent); }
  .brand-mark__name { font-weight: 700; font-size: 34px; letter-spacing: 4px; color: var(--accent); }
  .front-info {
    position: absolute; font-size: 17px; letter-spacing: 1.5px; line-height: 1.45; color: var(--silver-dim);
  }
  .front-info--left { left: 50px; top: 270px; }
  .front-info--right { right: 50px; top: 318px; text-align: right; }

  /* back */
  .company {
    position: absolute; top: 38px; left: 0; right: 0; text-align: center;
    font-weight: 700; font-size: 44px; letter-spacing: 5px; color: var(--silver-bright);
  }
  .person { position: absolute; left: 120px; top: 210px; text-align: right; width: 200px; }
  .person__name {
    font-family: "Oswald", sans-serif; font-weight: 600; font-size: 44px;
    letter-spacing: 1px; color: var(--silver); line-height: 1;
  }
  .person__title { font-size: 20px; color: var(--silver-dim); margin-top: 6px; letter-spacing: 1px; }
  .divider { position: absolute; left: 345px; top: 200px; width: 1px; height: 110px; background: var(--rule); }
  .contacts { position: absolute; left: 365px; top: 200px; list-style: none; }
  .contacts li {
    display: flex; align-items: center; gap: 8px;
    font-size: 17px; letter-spacing: .5px; line-height: 28px; color: var(--silver);
  }
  .contacts svg { width: 14px; height: 14px; flex: none; }
</style>
</head>
<body>

<section class="card card--front">
  <div class="tagline">
    WE PUT OUR HEART IN YOUR TRANSPORT
    <div class="tagline__sub">Licensed. Bonded. &amp; Insured.</div>
  </div>
  <div class="brand-mark">
    <span class="brand-mark__dot"></span>
    <span class="brand-mark__name">NORVANE</span>
  </div>
  <div class="front-info front-info--left">(877) BOOK NVT<br>US DOT 0000000</div>
  <div class="front-info front-info--right">(877) 555-0142<br>MC # 0000000</div>
</section>

<section class="card card--back">
  <h1 class="company">NORVANE TRANSPORT, INC.</h1>
  <div class="person">
    <div class="person__name">DALE MERCER</div>
    <div class="person__title">Transporter</div>
  </div>
  <div class="divider"></div>
  <ul class="contacts">
    <li>
      <svg viewBox="0 0 14 14" fill="none" stroke="#c9c9c9" stroke-width="1.4"><path d="M3 1.5 L5 1.5 L6 4.5 L4.5 5.5 C5.3 7.3 6.7 8.7 8.5 9.5 L9.5 8 L12.5 9 L12.5 11 C12.5 12 11.5 12.7 10.5 12.5 C6 11.6 2.4 8 1.5 3.5 C1.3 2.5 2 1.5 3 1.5 Z"/></svg>
      (404) 555-0187
    </li>
    <li>
      <svg viewBox="0 0 14 14" fill="none" stroke="#c9c9c9" stroke-width="1.4"><rect x="3.5" y="1" width="7" height="12" rx="1"/><line x1="6" y1="11" x2="8" y2="11"/></svg>
      (770) 555-0123
    </li>
    <li>
      <svg viewBox="0 0 14 14" fill="none" stroke="#c9c9c9" stroke-width="1.4"><rect x="1" y="3" width="12" height="8"/><path d="M1 3 L7 8 L13 3"/></svg>
      dale@norvanetransport.com
    </li>
    <li>
      <svg viewBox="0 0 14 14" fill="none" stroke="#c9c9c9" stroke-width="1.2"><circle cx="7" cy="7" r="5.8"/><ellipse cx="7" cy="7" rx="2.6" ry="5.8"/><line x1="1.2" y1="7" x2="12.8" y2="7"/></svg>
      www.norvanetransport.com
    </li>
  </ul>
</section>

</body>
</html>
```